Book cover for book about Climate Change

Looking for a clean, bold, and attractive cover for a mass-market paperback (5.5"x 8.5") about solving the climate change problem. Title is either "Where the Rivers Begin” or A Garden Left Standing” (your choice), subtitle is "A five-step plan to reverse climate change — to ensure that your grandchildren will live on a clean and comfortable planet," author is Milo Pardrey. Thinking that it *might* feature an image of Earth (or a portion thereof) and its very thin layer of atmosphere -- but STRONGLY encourage other ideas too!

Requirements
Nice to have
• Keep it positive — NOT scary doom-and-gloom

```html
<!DOCTYPE html>
<html lang="en">
<head>
<meta charset="UTF-8">
<title>Where the Rivers Begin — Book Cover</title>
<link href="https://fonts.googleapis.com/css2?family=Inter+Tight:wght@600;700&family=Barlow+Semi+Condensed:wght@600;700&display=swap" rel="stylesheet">
<style>
  :root {
    --backdrop: #efd6b2;
    --cover-plum: #3c0f35;
    --title-white: #ffffff;
    --accent-gold: #f2b81a;
    --earth-light: #9a9fca;
    --earth-mid: #5b5186;
  }
  * { margin: 0; padding: 0; box-sizing: border-box; }
  html, body {
    width: 1200px;
    height: 1200px;
    overflow: hidden;
    background: var(--backdrop);
  }
  .canvas {
    position: relative;
    width: 1200px;
    height: 1200px;
    background: var(--backdrop);
  }
  .cover {
    position: absolute;
    left: 342px;
    top: 92px;
    width: 585px;
    height: 905px;
    background: var(--cover-plum);
    overflow: hidden;
  }
  .author {
    position: absolute;
    top: 52px;
    left: 0;
    width: 100%;
    text-align: center;
    font-family: "Barlow Semi Condensed", "Arial Narrow", sans-serif;
    font-weight: 700;
    font-size: 50px;
    letter-spacing: 0.22em;
    padding-left: 0.22em;
    color: var(--accent-gold);
  }
  .earth-photo {
    position: absolute;
    left: 40px;
    top: 275px;
    width: 220px;
    height: 260px;
    z-index: 0;
    background: radial-gradient(ellipse 45% 50% at 35% 50%,
      var(--earth-light) 0%,
      var(--earth-mid) 45%,
      rgba(60, 15, 53, 0) 100%);
  }
  .title {
    position: absolute;
    z-index: 1;
    top: 205px;
    left: 0;
    width: 100%;
    text-align: center;
    font-family: "Inter Tight", "Helvetica Neue", Arial, sans-serif;
    font-weight: 700;
    font-size: 128px;
    line-height: 103px;
    letter-spacing: -6px;
    color: var(--title-white);
  }
  .title-line { display: block; }
  .title-line--accent { color: var(--accent-gold); }
  .subtitle {
    position: absolute;
    top: 732px;
    left: 0;
    width: 100%;
    text-align: center;
    font-family: "Barlow Semi Condensed", "Arial Narrow", sans-serif;
    font-weight: 700;
    font-size: 25px;
    line-height: 31px;
    color: var(--title-white);
  }
  .subtitle-accent { color: var(--accent-gold); }
</style>
</head>
<body>
<main class="canvas">
  <section class="cover">
    <p class="author">MILO PARDREY</p>

    <div class="earth-photo" role="img" aria-label="Photograph of Earth seen from space, its lit edge and thin atmosphere"></div>

    <h1 class="title">
      <span class="title-line">WHERE</span>
      <span class="title-line">THE</span>
      <span class="title-line">RIVERS</span>
      <span class="title-line title-line--accent">BEGIN</span>
    </h1>

    <p class="subtitle">
      A <span class="subtitle-accent">FIVE-STEP</span> PLAN TO <span class="subtitle-accent">REVERSE</span><br>
      CLIMATE CHANGE - TO ENSURE THAT YOUR<br>
      GRANDCHILDREN WILL LIVE ON A CLEAN<br>
      AND COMFORTABLE PLANET.
    </p>
  </section>
</main>
</body>
</html>
```